Business Card Design for Cybersecurity Company - Quorvent Systems

We need a business card design for our new cybersecurity company, Quorvent. We’re going for a clean, hi tech look that feels modern, premium, and trustworthy. We want a design that really stands out and makes people say WOW when we hand it over!

Quorvent delivers reliable IT support and managed services for small and mid sized businesses. We help companies stay secure, efficient, and connected through proactive monitoring, cybersecurity services, cloud management, and remote support.

Target Market(s)

Designers should target small and mid sized businesses that need dependable cybersecurity and IT support.

Industry/Entity Type

Cybersecurity, Managed Service Provider, IT services

Contact Information for Business Card

Contact information

Requirements
Must have
• The card should look clean, modern, and tech focused, with the Quorvent logo, clear contact info, and strong readability. It needs to feel premium and professional while still keeping a simple layout that fits a cybersecurity and IT brand.
Nice to have
• Nice to have elements include subtle touches that give the card a modern, tech feel, along with a layout that works well in different background styles.
Should not have
• The card should avoid clutter, loud graphics, or anything that takes attention away from the logo and contact details.

```html
<!DOCTYPE html>
<html lang="en">
<head>
<meta charset="utf-8">
<title>Quorvent Systems – Business Card</title>
<link href="https://fonts.googleapis.com/css2?family=Montserrat:wght@400;500;700&display=swap" rel="stylesheet">
<style>
  :root {
    --stage: #1e1e1e;
    --card: #232324;
    --card-back: #1f1f20;
    --pattern: #2a2a2c;
    --violet: #7a4cb3;
    --blue: #4b87d4;
    --accent: #5f6fd6;
    --text: #f2f2f4;
    --muted: #b9b9c4;
  }
  * { box-sizing: border-box; margin: 0; padding: 0; }
  html, body { width: 1200px; height: 900px; overflow: hidden; }
  body {
    background: var(--stage);
    font-family: "Montserrat", sans-serif;
    color: var(--text);
    position: relative;
  }
  .card {
    position: absolute;
    width: 660px;
    height: 377px;
    border-radius: 22px;
    overflow: hidden;
    box-shadow: 0 18px 40px rgba(0,0,0,.55);
  }

  /* Back side */
  .card--back { left: 90px; top: 60px; background: var(--card-back); }
  .card--back .pattern-field {
    position: absolute; inset: 0;
    background: radial-gradient(circle at 75% 30%, #2f2f32 0%, var(--card-back) 70%);
  }
  .card--back .brand {
    position: absolute; right: 70px; top: 150px;
    display: flex; align-items: center; gap: 14px;
  }
  .brand-dot {
    width: 44px; height: 44px; border-radius: 50%;
    background: var(--accent);
  }
  .brand-name {
    font-weight: 500; font-size: 30px; color: var(--accent); letter-spacing: .5px;
  }

  /* Front side */
  .card--front { left: 450px; top: 470px; background: var(--card); }
  .front-band {
    position: absolute; left: 0; top: 0; bottom: 0; width: 74px;
    background: linear-gradient(180deg, var(--violet) 0%, #6a55bb 55%, var(--blue) 100%);
  }
  .front-decor {
    position: absolute; right: 0; top: 0; width: 300px; height: 100%;
    background: radial-gradient(circle at 60% 45%, #2c2c2f 0%, var(--card) 75%);
  }
  .front-content {
    position: absolute; left: 110px; top: 38px; right: 40px;
  }
  .front-content .brand { display: flex; align-items: center; gap: 14px; margin-bottom: 42px; }
  .front-content .brand-dot { width: 52px; height: 52px; }
  .front-content .brand-name { font-size: 32px; }
  .person-name {
    font-weight: 700; font-size: 26px; color: var(--accent); letter-spacing: .5px;
  }
  .person-role { font-size: 15px; color: var(--text); margin-top: 2px; }
  .divider { width: 18px; height: 2px; background: var(--accent); margin: 16px 0 12px; }
  .contact-list { list-style: none; }
  .contact-list li {
    display: flex; align-items: center; gap: 10px;
    font-size: 15px; line-height: 26px; color: var(--text);
  }
  .contact-list svg { width: 14px; height: 14px; fill: var(--accent); flex: none; }
</style>
</head>
<body>

  <section class="card card--back" aria-label="Card back">
    <div class="pattern-field" role="img" aria-label="Repeating faint brand-mark pattern across the card back"></div>
    <div class="brand">
      <span class="brand-dot"></span>
      <span class="brand-name">Quorvent Systems</span>
    </div>
  </section>

  <section class="card card--front" aria-label="Card front">
    <div class="front-band"></div>
    <div class="front-decor" role="img" aria-label="Large faint brand-mark decoration with circuit lines"></div>
    <div class="front-content">
      <div class="brand">
        <span class="brand-dot"></span>
        <span class="brand-name">Quorvent Systems</span>
      </div>
      <h1 class="person-name">DANA WHITMORE</h1>
      <p class="person-role">Owner | CEO | Quorvent Systems</p>
      <div class="divider"></div>
      <ul class="contact-list">
        <li><svg viewBox="0 0 24 24"><path d="M6.6 10.8a15.1 15.1 0 0 0 6.6 6.6l2.2-2.2a1 1 0 0 1 1-.25 11.4 11.4 0 0 0 3.6.57 1 1 0 0 1 1 1V20a1 1 0 0 1-1 1A17 17 0 0 1 3 4a1 1 0 0 1 1-1h3.5a1 1 0 0 1 1 1c0 1.25.2 2.45.57 3.6a1 1 0 0 1-.25 1z"/></svg>(855) 410-QRVT</li>
        <li><svg viewBox="0 0 24 24"><path d="M6.6 10.8a15.1 15.1 0 0 0 6.6 6.6l2.2-2.2a1 1 0 0 1 1-.25 11.4 11.4 0 0 0 3.6.57 1 1 0 0 1 1 1V20a1 1 0 0 1-1 1A17 17 0 0 1 3 4a1 1 0 0 1 1-1h3.5a1 1 0 0 1 1 1c0 1.25.2 2.45.57 3.6a1 1 0 0 1-.25 1z"/></svg>(855) 410 7788</li>
        <li><svg viewBox="0 0 24 24"><path d="M7 1h10a2 2 0 0 1 2 2v18a2 2 0 0 1-2 2H7a2 2 0 0 1-2-2V3a2 2 0 0 1 2-2zm0 3v14h10V4zm5 15.5a1 1 0 1 0 0 2 1 1 0 0 0 0-2z"/></svg>(813) 555-0142</li>
        <li><svg viewBox="0 0 24 24"><path d="M2 5h20v14H2zm2 2v.5l8 5 8-5V7l-8 5z"/></svg>dana@quorvent.com</li>
        <li><svg viewBox="0 0 24 24"><path d="M12 2a10 10 0 1 0 0 20 10 10 0 0 0 0-20zm6.9 9h-3a15 15 0 0 0-1.2-5.6A8 8 0 0 1 18.9 11zM12 4.1c.9 1.2 1.7 3.6 1.9 6.9h-3.8c.2-3.3 1-5.7 1.9-6.9zM9.3 5.4A15 15 0 0 0 8.1 11h-3a8 8 0 0 1 4.2-5.6zM5.1 13h3a15 15 0 0 0 1.2 5.6A8 8 0 0 1 5.1 13zm6.9 6.9c-.9-1.2-1.7-3.6-1.9-6.9h3.8c-.2 3.3-1 5.7-1.9 6.9zm2.7-1.3a15 15 0 0 0 1.2-5.6h3a8 8 0 0 1-4.2 5.6z"/></svg>www.quorvent.com</li>
      </ul>
    </div>
  </section>

</body>
</html>
```